Brochure

I have a current booklet for Cedar Peak Labs, I need to incorporate additional information and testing into it. attached are the current inside pages and the additional items that need to be added.

Requirements
Must have
• matching the background, colors, and format of the original inside booklet pages.

```html
<!DOCTYPE html>
<html lang="en">
<head>
<meta charset="utf-8">
<title>Cedar Peak Labs – Urinary Tract Infection</title>
<link rel="stylesheet" href="https://fonts.googleapis.com/css2?family=Mulish:wght@400;500;700;800&display=swap">
<style>
  :root {
    --brand-blue: #1673c4;
    --navy: #1f4f8f;
    --ink: #3f4347;
    --tab-grey: #55585c;
    --sky: #5fb3e6;
    --faint: #edf3fa;
    --white: #ffffff;
  }
  * { box-sizing: border-box; margin: 0; padding: 0; }
  html, body { width: 986px; height: 1200px; overflow: hidden; background: var(--white); }
  body { font-family: "Mulish", Arial, sans-serif; color: var(--ink); }
  .page { position: relative; width: 986px; height: 1200px; overflow: hidden; background: var(--white); }

  .trim-tab {
    position: absolute; left: 0; top: 0; width: 53px; height: 1200px; background: var(--tab-grey);
  }
  .trim-tab span {
    position: absolute; left: 26px; top: 600px; white-space: nowrap;
    transform: translate(-50%, -50%) rotate(-90deg);
    color: var(--white); font-weight: 800; font-size: 17px; letter-spacing: 0.2px;
  }

  .backdrop { position: absolute; inset: 0; pointer-events: none; }

  .title {
    position: absolute; left: 129px; top: 98px;
    font-weight: 500; font-size: 47px; letter-spacing: 0.5px; color: var(--brand-blue);
  }

  .benefits { position: absolute; left: 121px; top: 220px; list-style: none; }
  .benefit { position: absolute; left: 0; display: flex; align-items: center; width: 440px; height: 74px; }
  .benefit svg { flex: none; width: 74px; height: 74px; }
  .benefit p { margin-left: 24px; font-size: 18.5px; line-height: 25px; }

  .photo {
    position: absolute; left: 639px; top: 213px; width: 225px; height: 225px; border-radius: 50%;
    background: radial-gradient(circle at 50% 40%, #e9eef2 0%, #c9d3db 55%, #9fb2c2 100%);
  }

  .targets { position: absolute; left: 606px; top: 452px; width: 290px; text-align: center; }
  .targets h2 { font-weight: 800; font-size: 18px; color: var(--brand-blue); letter-spacing: 0.3px; }
  .targets p { margin-top: 8px; font-size: 19px; line-height: 25.5px; }

  .panel { position: absolute; top: 608px; width: 297px; }
  .panel h3 {
    height: 34px; line-height: 34px; padding-left: 21px; background: var(--navy);
    color: var(--white); font-weight: 800; font-size: 18px;
  }
  .panel ul { list-style: none; padding: 12px 0 0 21px; font-size: 15.6px; }
  .panel.bacteria { left: 297px; }
  .panel.bacteria li { line-height: 20.3px; }
  .panel.fungi { left: 600px; }
  .panel.fungi li { line-height: 21.9px; }
</style>
</head>
<body>
<div class="page">

  <svg class="backdrop" width="986" height="1200" viewBox="0 0 986 1200" aria-hidden="true">
    <defs>
      <linearGradient id="sweep" x1="0" y1="0" x2="1" y2="0">
        <stop offset="0" stop-color="#1e6fc0"/>
        <stop offset="0.55" stop-color="#3d93d6"/>
        <stop offset="1" stop-color="#8cc9ef"/>
      </linearGradient>
    </defs>
    <circle cx="990" cy="1000" r="245" fill="none" stroke="var(--faint)" stroke-width="24"/>
    <path d="M53 1075 C 300 1120, 600 1165, 840 1200 L 53 1200 Z" fill="url(#sweep)"/>
    <path d="M300 1130 C 550 1160, 800 1185, 986 1178 L 986 1200 L 600 1200 C 500 1175, 400 1150, 300 1130 Z" fill="#a9d8f3" opacity="0.7"/>
  </svg>

  <div class="trim-tab"><span>Tabs Here - This portion will be trimmed off</span></div>

  <h1 class="title">URINARY TRACT INFECTION</h1>

  <ul class="benefits">
    <li class="benefit" style="top:0">
      <svg viewBox="0 0 74 74"><circle cx="37" cy="37" r="37" fill="var(--brand-blue)"/>
        <g fill="none" stroke="#fff" stroke-width="2.2"><circle cx="37" cy="37" r="15"/><path d="M23 22 A21 21 0 0 1 58 33"/><path d="M51 52 A21 21 0 0 1 16 41"/><path d="M42 31 C40 28 32 28 32 33 C32 38 42 36 42 41 C42 46 34 46 32 43 M37 25 V49"/></g></svg>
      <p>Cost effective to help maximize<br>your labs profits</p>
    </li>
    <li class="benefit" style="top:84px">
      <svg viewBox="0 0 74 74"><circle cx="37" cy="37" r="37" fill="var(--brand-blue)"/>
        <g fill="none" stroke="#fff" stroke-width="2.2"><circle cx="37" cy="40" r="16"/><path d="M33 20 H41 M37 20 V24 M37 30 V40 L43 46"/></g></svg>
      <p>5 minute run time ensures faster<br>turnaround times.</p>
    </li>
    <li class="benefit" style="top:168px">
      <svg viewBox="0 0 74 74"><circle cx="37" cy="37" r="37" fill="var(--brand-blue)"/>
        <g fill="none" stroke="#fff" stroke-width="2.2"><circle cx="37" cy="37" r="6"/><path d="M34 19 H40 L41 24 L46 26 L50 23 L54 27 L51 31 L53 36 L55 37 V40 L53 41 L51 45 L54 49 L50 53 L46 50 L41 52 L40 55 H34 L33 52 L28 50 L24 53 L20 49 L23 45 L21 41 L19 40 V37 L21 36 L23 31 L20 27 L24 23 L28 26 L33 24 Z"/></g></svg>
      <p>Compatible with ALL<br>PCR MACHINES</p>
    </li>
    <li class="benefit" style="top:252px">
      <svg viewBox="0 0 74 74"><circle cx="37" cy="37" r="37" fill="var(--brand-blue)"/>
        <g fill="none" stroke="#fff" stroke-width="2"><path d="M20 52 H52 M24 50 V40 M29 50 V36 M34 50 V32 M39 50 V26 M44 44 V22"/><path d="M20 24 H50" stroke-dasharray="2 2"/><circle cx="49" cy="49" r="6"/></g></svg>
      <p>Highly demanded targets to make<br>your lab more appealing to providers</p>
    </li>
  </ul>

  <div class="photo" role="img" aria-label="Photo of a smiling doctor in a white coat reading a tablet"></div>

  <section class="targets">
    <h2>28 TARGETS</h2>
    <p>A provider’s #1 priority is their patients. When you bring them more targets, you are providing them better tools for treatment</p>
  </section>

  <section class="panel bacteria">
    <h3>BACTERIA</h3>
    <ul>
      <li>Escherichia coli</li><li>Streptococcus agalactiae</li><li>Klebsiella oxytoca</li>
      <li>Staphylococcus saprophyticus</li><li>Serratia marcescens</li><li>Proteus mirabilis</li>
      <li>Aerococcus urinae</li><li>Treponema pallidum</li><li>Enterobacter cloacae</li>
      <li>Pseudomonas aeruginosa</li><li>Citrobacter freundii</li><li>Klebsiella aerogenes</li>
      <li>Klebsiella pneumoniae</li><li>Morganella morganii</li><li>Corynebacterium urealyticum</li>
      <li>Enterococcus faecium</li><li>Enterococcus faecalis</li><li>Acinetobacter baumannii</li>
      <li>Proteus vulgaris</li><li>Staphylococcus aureus</li><li>Ureplasma</li><li>Providencia stuartii</li>
    </ul>
  </section>

  <section class="panel fungi">
    <h3>Fungi</h3>
    <ul>
      <li>Candida parapsilosis</li><li>Candida glabrata</li><li>Candida auris</li>
      <li>Candida tropicalis</li><li>Candida krusei</li><li>Candida albicans</li>
    </ul>
  </section>

</div>
</body>
</html>
```